I want to sell a virtual ticket that captures customers details.

Using this information, i manually write the customers details on a piece of paper and enter them into a draw/raffle to potentially win a watch. I dont need random generators/software to pick winners, as law mandates this process to be physically done. All i need is a nice website that allows customers to purchase and enter. I have posted a few links below in the description. If you refer to brightcanoparade.com, you will see what i am after. I have my own site www.themarbleparlourhouse.com.au but i dont like how it looks and i want something better. I hope this will give you an idea on what i am after.

Target Market(s)

adults aged approximately 24-56

Industry/Entity Type

luxury watches / contestant giveaways

Number of Pages Required

4 page

Font styles to use
Serif
Other font styles liked:
• something classy - i am not sure

Colors

Designer to choose only greyscale colors for use in the design.

Requirements
Must have
• Stripe payment software

```html
<!DOCTYPE html>
<html lang="en">
<head>
<meta charset="utf-8">
<title>The Velvet Dial Club</title>
<link href="https://fonts.googleapis.com/css2?family=Playfair+Display:wght@400;700&family=Merriweather+Sans:wght@300;400;700&display=swap" rel="stylesheet">
<style>
:root{
  --navy:#0d2d55;
  --ink:#1a1a1a;
  --text:#333;
  --muted:#555;
  --panel:#dcdcdc;
  --band:#f2f2f2;
  --gold:#d9a21b;
  --white:#fff;
  --serif:'Playfair Display', Georgia, serif;
  --sans:'Merriweather Sans', Arial, sans-serif;
}
*{box-sizing:border-box;margin:0;padding:0}
html,body{width:1200px;height:2876px;overflow:hidden;background:var(--white)}
body{position:relative;font-family:var(--sans);color:var(--text)}
.abs{position:absolute}
/* header */
.hero-panel{left:928px;top:0;width:272px;height:600px;background:var(--panel)}
.nav-left{left:150px;top:43px;font-size:13px;color:var(--ink)}
.brand{left:480px;top:40px;width:240px;text-align:center;font-size:14px;font-weight:700;letter-spacing:1.5px;text-transform:uppercase;color:var(--ink)}
.nav{right:150px;top:42px;display:flex;gap:26px;font-size:15px;color:var(--ink)}
.nav .active{color:var(--navy)}
.hero-frame{left:715px;top:97px;width:424px;height:459px;border:1.5px solid #a8a8a8;background:var(--white);padding:18px}
.hero-photo{width:100%;height:100%;background:linear-gradient(160deg,#f4f4f4 0%,#b8b8b8 45%,#6f7480 70%,#c9c9c9 100%)}
.hero-title{left:150px;top:172px;font-family:var(--serif);font-weight:700;font-size:50px;line-height:61px;color:var(--ink)}
.hero-sub{left:150px;top:307px;font-size:15px;color:var(--ink)}
.btn-solid{left:150px;top:356px;width:142px;height:42px;background:var(--navy);color:var(--white);font-size:13px;display:flex;align-items:center;justify-content:center;gap:6px}
.countdown{left:150px;top:429px;width:420px;height:82px;background:var(--navy);display:flex;align-items:center;box-shadow:0 4px 12px rgba(0,0,0,.15)}
.count-cell{flex:1;text-align:center;color:var(--white);font-family:var(--serif);font-size:16px;line-height:22px;border-right:1px solid rgba(255,255,255,.4)}
.count-cell:last-child{border:none}
.count-cell b{display:block;font-weight:400;font-size:22px}
.tickets{left:570px;top:429px;width:105px;height:82px;background:var(--white);box-shadow:0 4px 12px rgba(0,0,0,.1);text-align:center;padding-top:18px;font-family:var(--serif);font-size:16px;line-height:24px;color:var(--ink)}
.tickets b{display:block;font-weight:400;font-size:22px}
/* about */
.about-photo{left:173px;top:700px;width:322px;height:360px;border:1px solid #999;background:linear-gradient(180deg,#b9b7b5 0%,#8f8a86 55%,#6e6862 100%)}
.heading{font-family:var(--serif);font-weight:400;font-size:34px;color:var(--ink);display:flex;align-items:center;gap:30px}
.heading::after{content:"";width:150px;height:2px;background:var(--navy)}
.about-head{left:584px;top:668px}
.about-copy{left:584px;top:726px;width:470px;font-size:13.3px;line-height:22.5px;color:var(--ink);font-weight:300}
.about-copy p{margin-bottom:22.5px}
.btn-outline{left:584px;top:1042px;width:168px;height:42px;border:2px solid var(--navy);color:var(--navy);font-size:13px;display:flex;align-items:center;justify-content:center;gap:6px}
/* values */
.values{left:0;top:1160px;width:1200px;height:487px;background:var(--band)}
.values-head{left:527px;top:1188px}
.value{width:200px;text-align:center;font-weight:700;font-size:19px;color:var(--ink)}
.values-photo{left:555px;top:1296px;width:167px;height:300px;background:linear-gradient(180deg,#9a9a9a 0%,#5c6270 50%,#9a9a9a 100%)}
/* how */
.how-head{left:512px;top:1720px}
.how-sub{left:0;width:1200px;top:1772px;text-align:center;font-size:18px;color:var(--ink)}
.step-label{width:300px;text-align:center;font-size:19px;color:var(--ink)}
/* packages */
.pkg-head{left:506px;top:2095px}
.card{top:2208px;width:208px;height:337px;background:var(--white);box-shadow:0 4px 14px rgba(0,0,0,.07);text-align:center}
.card-top{height:52px;background:var(--ink);border-top-color:var(--ink);color:var(--white);font-size:15px;font-weight:700;display:flex;flex-direction:column;justify-content:center;position:relative}
.card-top small{font-weight:400;font-size:13px}
.card-top::after{content:"";position:absolute;left:50%;bottom:-7px;margin-left:-7px;border:7px solid transparent;border-bottom:none;border-top-color:inherit}
.card.navy .card-top{background:var(--navy);border-top-color:var(--navy)}
.price{margin-top:22px;font-size:54px;font-weight:700;color:var(--ink);line-height:66px}
.entries{margin-top:12px;font-size:13px;display:flex;justify-content:center;align-items:center;gap:6px}
.divider{margin:20px auto 0;width:160px;height:1px;background:#888}
.cause{margin-top:26px;font-size:13px;color:var(--muted)}
.enter{margin:22px auto 0;width:187px;height:42px;background:var(--ink);color:var(--white);font-size:13.5px;display:flex;align-items:center;justify-content:center}
.card.navy .enter{background:var(--navy)}
.badge{left:500px;top:2197px;background:var(--ink);color:var(--white);font-size:12px;padding:3px 14px}
/* footer */
.footer{left:0;top:2620px;width:1200px;height:216px;background:var(--band)}
.footer-brand{left:150px;top:2703px;font-size:13px;font-weight:700;letter-spacing:1.2px;text-transform:uppercase;color:var(--ink)}
.social{top:2750px;width:30px;height:30px;border-radius:50%;background:var(--navy)}
.foot-col h4{font-size:15px;font-weight:400;color:var(--ink);margin-bottom:16px}
.foot-col li{list-style:none;font-size:13px;color:var(--muted);line-height:27px}
.foot-col p{font-size:13px;color:var(--muted);line-height:21px}
.email{left:824px;top:2777px;width:182px;height:38px;border:1px solid #888;background:var(--white);font-size:12px;color:var(--muted);padding:11px 13px}
.email-btn{left:1006px;top:2777px;width:44px;height:38px;background:var(--navy);display:flex;align-items:center;justify-content:center}
.copyright{left:0;top:2836px;width:1200px;height:40px;background:var(--ink);color:#ddd;font-size:12.5px;display:flex;align-items:center;justify-content:center}
</style>
</head>
<body>

<!-- header / hero -->
<div class="abs hero-panel"></div>
<div class="abs nav-left">Latest Winners</div>
<div class="abs brand">The Velvet Dial Club</div>
<nav class="abs nav"><span class="active">Home</span><span>FAQ</span><span>Contact US</span></nav>
<div class="abs hero-frame"><div class="hero-photo" role="img" aria-label="Photo of a steel diver's wristwatch with a blue-to-black dial"></div></div>
<h1 class="abs hero-title">Your Chance to Win<br>Starts here.</h1>
<p class="abs hero-sub">Supporting Health &amp; Making Wealth</p>
<div class="abs btn-solid">SUBSCRIBE <span>→</span></div>
<div class="abs countdown">
  <div class="count-cell"><b>1</b>days</div>
  <div class="count-cell"><b>10</b>hours</div>
  <div class="count-cell"><b>34</b>min</div>
  <div class="count-cell"><b>21</b>Sec</div>
</div>
<div class="abs tickets"><b>91</b>tickets left</div>

<!-- about -->
<svg class="abs" style="left:0;top:0" width="1200" height="1100" aria-hidden="true">
  <polyline points="343,677 150,677 150,876" fill="none" stroke="#1a1a1a" stroke-width="2"/>
  <polyline points="518,887 518,1084 325,1084" fill="none" stroke="#1a1a1a" stroke-width="2"/>
</svg>
<div class="abs about-photo" role="img" aria-label="Photo of a chronograph wristwatch with a blue dial resting on a wooden table"></div>
<h2 class="abs heading about-head">About Us</h2>
<div class="abs about-copy">
  <p>We are a group of friends from Melbourne, Australia who all share a common passion – a love for watches. We aim to provide an equal opportunity for all watches lovers in Australia, whilst, more importantly, paving the way for a cleaner, eco-friendlier world.</p>
  <p>We strongly believe that all communities, regardless of interests, should share a common goal, which is why we have joined forces with (TO BE CONFIRMED), whose main aim is to help plant trees across Australia to prevent deforestation in our backyard.</p>
  <p>Our services are one of a kind, as each package sold goes towards planting trees in the much-needed regions of Australia. We hope you are excited as we are, as we embark on this journey together!</p>
</div>
<div class="abs btn-outline">OUR PACKAGES <span>→</span></div>

<!-- values -->
<div class="abs values"></div>
<h2 class="abs heading values-head">Our Values</h2>
<svg class="abs" style="left:0;top:1160px" width="1200" height="487" aria-hidden="true" fill="none" stroke="#1a1a1a" stroke-width="1.5">
  <path d="M349 176H486"/><path d="M486 176L560 240" stroke-dasharray="12 14"/>
  <path d="M906 176H769"/><path d="M769 176L695 240" stroke-dasharray="12 14"/>
  <path d="M349 418H486"/><path d="M486 418L560 354" stroke-dasharray="12 14"/>
  <path d="M906 418H769"/><path d="M769 418L695 354" stroke-dasharray="12 14"/>
  <g stroke="#0d2d55" stroke-width="2">
    <rect x="258" y="125" width="10" height="22"/><rect x="303" y="125" width="10" height="22"/>
    <path d="M268 130l18-6 17 6M272 144l12-12 14 10"/>
    <path d="M953 124l12 0 12 12-12 12-12-12z"/><path d="M964 140c-4-4 0-9 4-5 4-4 8 1 4 5l-4 4z"/>
    <circle cx="258" cy="387" r="12"/><path d="M258 380v8l5 4"/>
    <circle cx="957" cy="381" r="6"/><path d="M945 399c0-8 6-11 12-11s12 3 12 11z"/><path d="M968 387l8-2 8 2v5c0 5-4 7-8 9-4-2-8-4-8-9z"/>
  </g>
</svg>
<div class="abs value" style="left:185px;top:1322px">RESPECT</div>
<div class="abs value" style="left:868px;top:1322px">LOYALTY</div>
<div class="abs value" style="left:158px;top:1564px">COMMITMENT</div>
<div class="abs value" style="left:860px;top:1564px">TRUST</div>
<div class="abs values-photo" role="img" aria-label="Photo of a steel diver's wristwatch with a blue gradient dial"></div>

<!-- how to play -->
<h2 class="abs heading how-head">How to Play</h2>
<p class="abs how-sub">IT’S THAT SIMPLE!</p>
<svg class="abs" style="left:0;top:1830px" width="1200" height="140" aria-hidden="true">
  <path d="M150 27H1050" stroke="#1a1a1a" stroke-width="2.5"/>
  <path d="M444 21l6 6-6 6M744 21l6 6-6 6" fill="none" stroke="#1a1a1a" stroke-width="2"/>
  <g font-family="Merriweather Sans, Arial, sans-serif" font-size="12" font-weight="700" fill="#fff" text-anchor="middle">
    <circle cx="300" cy="27" r="14" fill="#000"/><text x="300" y="31">1</text>
    <circle cx="600" cy="27" r="14" fill="#000"/><text x="600" y="31">2</text>
    <circle cx="900" cy="27" r="14" fill="#000"/><text x="900" y="31">3</text>
  </g>
  <g fill="none" stroke="#0d2d55" stroke-width="2">
    <rect x="276" y="81" width="48" height="48" rx="3"/><path d="M283 92h34M283 104h34v18h-34zM283 113h34"/>
    <path d="M580 80h20l20 20v30h-40z"/><path d="M600 80v20h20M588 108h16v14h-16z"/>
    <path d="M885 84h30l-4 22c-2 6-7 9-11 9s-9-3-11-9z"/><path d="M885 88h-10c0 8 5 12 12 14M915 88h10c0 8-5 12-12 14M900 115v10M890 130h20"/><path d="M900 90l3 6 6 1-4 4 1 6-6-3-6 3 1-6-4-4 6-1z"/>
  </g>
</svg>
<div class="abs step-label" style="left:150px;top:1998px">Enter Details</div>
<div class="abs step-label" style="left:450px;top:1998px">Choose a Package</div>
<div class="abs step-label" style="left:750px;top:1998px">Wait for Draw</div>

<!-- packages -->
<h2 class="abs heading pkg-head">Our Package</h2>
<svg class="abs" style="left:928px;top:2175px" width="42" height="32" aria-hidden="true"><path d="M3 22L7 6l9 9 5-13 5 13 9-9 4 16z M5 25h32v4H5z" fill="#d9a21b"/></svg>

<div class="abs card" style="left:150px">
  <div class="card-top">BRONZE</div>
  <div class="price">$7</div>
  <div class="entries"><svg width="13" height="13" aria-hidden="true"><circle cx="6.5" cy="6.5" r="6.5" fill="#0d2d55"/><path d="M3.5 6.5l2 2 4-4" stroke="#fff" stroke-width="1.6" fill="none"/></svg>1 Entry</div>
  <div class="divider"></div>
  <div class="cause">Help with other supplies</div>
  <div class="enter">Enter the Competition</div>
</div>
<div class="abs card navy" style="left:382px">
  <div class="card-top">SILVER</div>
  <div class="price">$12</div>
  <div class="entries"><svg width="13" height="13" aria-hidden="true"><circle cx="6.5" cy="6.5" r="6.5" fill="#0d2d55"/><path d="M3.5 6.5l2 2 4-4" stroke="#fff" stroke-width="1.6" fill="none"/></svg>2 Entries</div>
  <div class="divider"></div>
  <div class="cause">Help build a Koala’s Home</div>
  <div class="enter">Enter the Competition</div>
</div>
<div class="abs badge">Popular</div>
<div class="abs card" style="left:614px">
  <div class="card-top">GOLD</div>
  <div class="price">$16</div>
  <div class="entries"><svg width="13" height="13" aria-hidden="true"><circle cx="6.5" cy="6.5" r="6.5" fill="#1a1a1a"/><path d="M3.5 6.5l2 2 4-4" stroke="#fff" stroke-width="1.6" fill="none"/></svg>3 Entries</div>
  <div class="divider"></div>
  <div class="cause">Help us fight deforestation</div>
  <div class="enter">Enter the Competition</div>
</div>
<div class="abs card navy" style="left:845px">
  <div class="card-top">DELUXE<small>Fan favourite + Best odds</small></div>
  <div class="price">$19</div>
  <div class="entries"><svg width="13" height="13" aria-hidden="true"><circle cx="6.5" cy="6.5" r="6.5" fill="#0d2d55"/><path d="M3.5 6.5l2 2 4-4" stroke="#fff" stroke-width="1.6" fill="none"/></svg>5 Entries</div>
  <div class="divider"></div>
  <div class="cause">Help plant a tree</div>
  <div class="enter">Enter the Competition</div>
</div>

<!-- footer -->
<footer>
  <div class="abs footer"></div>
  <div class="abs footer-brand">The Velvet Dial Club</div>
  <div class="abs social" style="left:151px" role="img" aria-label="Social link"></div>
  <div class="abs social" style="left:196px" role="img" aria-label="Social link"></div>
  <div class="abs social" style="left:241px" role="img" aria-label="Social link"></div>
  <div class="abs foot-col" style="left:403px;top:2659px"><h4>Quick Links</h4><ul><li>FAQs</li><li>Contact Us</li><li>Terms &amp; Conditions</li></ul></div>
  <div class="abs foot-col" style="left:643px;top:2659px"><h4>Packages</h4><ul><li>Bronze</li><li>Silver</li><li>Gold</li><li>Deluxe</li></ul></div>
  <div class="abs foot-col" style="left:824px;top:2659px;width:226px"><h4>Newsletter</h4><p>Subscribe to our newsletter to get updates about contest.</p></div>
  <div class="abs email">Enter Your Email Address</div>
  <div class="abs email-btn"><svg width="16" height="16" aria-hidden="true"><path d="M1 8l14-7-4 14-3-5z" fill="#fff"/></svg></div>
  <div class="abs copyright">© 2021 The Velvet Dial Club | All Rights Reserved</div>
</footer>

</body>
</html>
```